Artificial Intelligence and Machine Learning Company Needs a New Website

We need a new web design for one of the leading companies in the Spanish market in the development of advanced analytics and artificial intelligence.
Our goal is to help in resolving complex planning decisions and improving the operational efficiency of our clients. We have big clients from different industries and very powerful technology partners. We want our new website to be clear and show our great experience in the sector (more than 10 years) and our young spirit.
Number of Pages Required
5+ page
Colors
Designer to choose colors to be used in the design.
Look and feel
Each slider illustrates characteristics of the customer's brand and the style your logo design should communicate.

```html
<!DOCTYPE html>
<html lang="en">
<head>
<meta charset="utf-8">
<title>clarion — planning, optimization, decision management</title>
<link rel="stylesheet" href="https://fonts.googleapis.com/css2?family=Poppins:wght@300;400;500;600&family=Montserrat:wght@600;700;800&display=swap">
<style>
:root{
  --orange:#e84e1c;
  --magenta:#c22ad6;
  --navy:#0b0d2a;
  --dark:#232325;
  --ink:#1d1d1f;
  --text:#555;
  --muted:#9a9a9a;
  --light:#f4f4f5;
  --white:#fff;
}
*{box-sizing:border-box;margin:0;padding:0}
html,body{width:1200px;height:5391px;overflow:hidden}
body{font-family:"Poppins",sans-serif;color:var(--ink);background:var(--white);position:relative}
.abs{position:absolute}
.brand{font-family:"Poppins",sans-serif;font-weight:500;font-size:38px;color:var(--orange);display:flex;align-items:center;gap:10px;letter-spacing:-.5px}
.brand i{display:inline-block;width:12px;height:12px;border-radius:50%;background:var(--magenta)}
/* hero */
.hero{position:absolute;left:0;top:0;width:1200px;height:785px;background:var(--navy)}
.hero-art{position:absolute;left:430px;top:90px;width:770px;height:600px;background:radial-gradient(ellipse at 45% 55%,#0f6f8a 0%,#0a2c4d 35%,rgba(11,13,42,0) 70%)}
.nav{position:absolute;left:130px;top:40px;right:130px;height:46px;display:flex;align-items:center}
.nav ul{display:flex;list-style:none;gap:34px;margin-left:70px;font-size:13px;color:#d8d8e4}
.nav li .dot{color:var(--orange);margin-left:4px}
.nav .search{margin-left:auto;width:26px;height:26px;border-radius:50%;border:2px solid var(--orange)}
.nav .join{margin-left:14px;background:var(--magenta);color:#fff;font-size:12px;padding:5px 18px;border-radius:14px}
.hero h1{position:absolute;left:126px;top:268px;font-weight:500;font-size:39px;line-height:45px;color:#fff}
.hero h1 span{color:var(--orange)}
.hero .sub{position:absolute;left:126px;top:435px;font-size:13px;color:#fff;font-weight:500}
.slider{position:absolute;left:130px;top:605px;font-size:15px;color:#fff;display:flex;gap:16px;align-items:center}
.slider b{color:var(--orange);font-weight:400}
/* who */
.who h2{position:absolute;left:132px;top:882px;font-size:38px;font-weight:500}
.who p{position:absolute;left:130px;width:620px;font-size:11.5px;line-height:25px;color:var(--text)}
.who-deco{position:absolute;left:848px;top:895px;width:285px;height:195px;background:linear-gradient(135deg,#f2f2f3,#e9e9ea);border-radius:6px}
/* industries */
.ind{position:absolute;width:400px;height:265px;overflow:hidden}
.ind .photo{position:absolute;inset:0;background:linear-gradient(135deg,#5d6572,#2f3640)}
.ind h3{position:absolute;left:45px;top:118px;color:#fff;font-size:27px;font-weight:400}
.ind.purple{background:var(--magenta)}
.ind.purple h3{top:70px;line-height:38px}
.ind.purple h3 b{font-family:"Montserrat",sans-serif;font-weight:700;letter-spacing:3px;font-size:34px}
.link{display:flex;align-items:center;gap:10px;font-size:11px;color:#fff}
.pill{display:inline-block;width:36px;height:16px;border-radius:8px;background:#fff;position:relative}
.pill::after{content:"→";position:absolute;left:11px;top:-3px;font-size:13px;color:var(--orange)}
.orange-box{position:absolute;left:415px;top:1229px;width:370px;height:235px;background:var(--orange)}
/* section titles */
.sec-title{position:absolute;left:0;width:1200px;text-align:center;font-size:38px;font-weight:500}
.sec-lead{position:absolute;left:280px;width:640px;text-align:center;font-size:11.5px;line-height:25px;color:var(--text)}
.card{position:absolute;width:296px;background:#fff;box-shadow:0 4px 18px rgba(0,0,0,.07);padding:40px 34px}
.card svg{width:50px;height:50px}
.card h4{font-size:17px;font-weight:400;line-height:25px;margin-top:22px;color:var(--ink);white-space:nowrap}
.card h4.wrap{white-space:normal}
.card .arrow{color:var(--orange);font-size:16px;margin-top:22px}
.card.on{background:var(--orange)}
.card.on h4{color:#fff}
.card.on .link{margin-top:22px}
/* how */
.how{position:absolute;left:21px;top:2362px;width:1154px;height:423px;background:linear-gradient(90deg,#3b3f45,#25272b 55%,#16171a)}
.how-photo{position:absolute;left:600px;top:2362px;width:575px;height:423px;background:radial-gradient(ellipse at 30% 45%,#4a3e39,#1b1b1e 70%)}
.how-tab{position:absolute;left:599px;top:2328px;width:576px;height:63px;background:var(--orange);color:#fff;font-family:"Montserrat",sans-serif;font-weight:700;letter-spacing:2px;font-size:15px;padding:24px 35px}
.how-line{position:absolute;left:21px;top:2777px;width:578px;height:8px;background:var(--orange)}
.step{position:absolute;top:2525px;width:230px;color:#fff}
.step .num{position:absolute;right:20px;top:-8px;font-size:38px;color:rgba(255,255,255,.35);font-weight:300}
.step h5{font-size:19px;font-weight:500;margin-top:14px}
.step p{font-size:12px;color:#aaa;margin-top:8px}
.step .d{font-size:15px;color:#ddd;margin-top:6px}
/* tech */
.tech-bg{position:absolute;left:21px;top:2785px;width:1154px;height:743px;background:var(--light)}
.tcard{height:201px;padding:38px 34px}
.tcard h4{margin-top:16px}
.tcard .arrow{margin-top:18px}
/* testimonial */
.testi{position:absolute;left:21px;top:3528px;width:1154px;height:335px;background:var(--dark)}
.testi h2{position:absolute;left:110px;top:95px;color:#fff;font-size:28px;font-weight:400;line-height:42px}
.testi h2 b{font-family:"Montserrat",sans-serif;font-weight:800;letter-spacing:4px;font-size:32px}
.quote-card{position:absolute;left:599px;top:3629px;width:368px;height:360px;background:var(--orange);padding:50px 42px;color:#fff}
.quote-card .who-line{display:flex;gap:16px;align-items:center}
.avatar{width:42px;height:42px;border-radius:50%;background:#f4d7cc}
.quote-card h6{font-family:"Montserrat",sans-serif;font-size:13px;letter-spacing:2px}
.quote-card small{font-size:10px;letter-spacing:1.5px}
.quote-card p{font-size:11.5px;font-weight:500;line-height:26px;margin-top:30px}
.quote-card .qm{position:absolute;right:34px;top:40px;font-family:"Montserrat",sans-serif;font-size:80px;line-height:60px;color:#ff9a76}
.pager{display:flex;gap:8px;margin-top:38px}
.pager i{width:8px;height:8px;border-radius:50%;border:1.5px solid #fff}
.pager i:first-child{background:#fff}
/* partners */
.partners-label{position:absolute;left:130px;top:4023px;font-size:16px;color:var(--muted);display:flex;align-items:center;gap:14px}
.partners-label::after{content:"";width:70px;height:1px;background:#e2e2e2}
.plogo{position:absolute;top:4077px;width:216px;height:107px;background:#fff;box-shadow:0 3px 14px rgba(0,0,0,.06);display:flex;align-items:center;justify-content:center;gap:10px;font-size:24px;color:#8b8b8b}
.plogo i{width:20px;height:20px;background:#c9c9c9}
/* news */
.news{position:absolute;top:4433px;width:295px;height:337px;overflow:hidden;background:linear-gradient(160deg,#6d6f73,#2e3034)}
.news .inner{position:absolute;left:20px;top:20px;right:20px;bottom:20px;background:var(--orange)}
.news .txt{position:absolute;left:33px;bottom:65px;color:#fff;width:230px}
.news small{font-family:"Montserrat",sans-serif;font-size:10px;font-weight:700;letter-spacing:1px}
.news p{font-size:15px;line-height:29px;margin-top:12px}
.news .link{margin-top:16px}
/* footer */
.footer{position:absolute;left:0;top:4858px;width:1200px;height:533px;background:var(--dark);color:#cfcfcf}
.contact{position:absolute;left:130px;top:190px;font-size:11.5px;line-height:20px}
.contact div{display:flex;gap:12px;margin-bottom:16px}
.contact svg{width:13px;height:13px;flex:none;margin-top:3px}
.contact a{color:#5b8cff;text-decoration:none}
.form{position:absolute;left:608px;top:115px;width:456px}
.form h6{font-family:"Montserrat",sans-serif;font-size:14px;letter-spacing:2px;color:#fff;font-weight:600}
.field{border-bottom:1px solid #4a4a4c;font-size:10.5px;color:#aaa;padding-bottom:12px}
.row{display:flex;gap:22px;margin-top:36px}
.row .field{flex:1}
.send{display:flex;align-items:center;gap:14px;margin-top:60px;font-family:"Montserrat",sans-serif;font-size:12px;letter-spacing:1.5px;color:#fff;font-weight:600}
.bottom{position:absolute;left:130px;right:136px;top:482px;display:flex;font-size:11px;color:#999}
.bottom nav{margin-left:auto;display:flex;gap:22px}
.bottom nav .cur{color:var(--orange)}
</style>
</head>
<body>

<header class="hero">
  <div class="hero-art" role="img" aria-label="Glowing wireframe figure in a virtual reality headset touching a DNA helix"></div>
  <nav class="nav">
    <div class="brand">clarion <i></i></div>
    <ul>
      <li>Industries<span class="dot">•</span></li>
      <li>Technologies<span class="dot">•</span></li>
      <li>About Us<span class="dot">•</span></li>
      <li>Resources</li>
      <li>Partners</li>
    </ul>
    <span class="search"></span>
    <span class="join">Join Us</span>
  </nav>
  <h1>planning,<br><span>optimization,</span><br>decision management</h1>
  <p class="sub">Advance Analytics &amp; Artificial Intelligence for Smart Decision</p>
  <div class="slider"><span>&lsaquo;</span><span><b>2</b> / 5</span><span style="color:var(--orange)">&rsaquo;</span></div>
</header>

<section class="who">
  <h2>who we are</h2>
  <p style="top:950px">Mei an iracundia conceptam, cu agam cetero has, saperet partiendo posidonium mea ne. Sed idque persequeris accommodare cu. Eu imperdiet assueverit appellantur sea. Debet viderer appetere te duo, alii legimus suavitate pro ea.</p>
  <p style="top:1053px">Te has dicat ceteros mediocrem, nec an luptatum praesent. Legere legimus fabellas in nam, exerci tempor eirmod no eum.</p>
  <div class="who-deco" role="img" aria-label="Faint grey decorative graphic"></div>
</section>

<section>
  <div class="ind purple" style="left:0;top:1214px">
    <h3>areas &amp;<br><b>INDUSTRIES</b></h3>
    <div class="link abs" style="left:45px;top:170px">view all industries <span class="pill"></span></div>
  </div>
  <div class="ind" style="left:400px;top:1214px"><div class="photo" role="img" aria-label="Field service technicians at work"></div></div>
  <div class="orange-box">
    <h3 class="abs" style="left:34px;top:100px;color:#fff;font-size:27px;font-weight:400">field services</h3>
    <div class="link abs" style="left:34px;top:150px">Learn More <span class="pill"></span></div>
  </div>
  <div class="ind" style="left:800px;top:1214px"><div class="photo" role="img" aria-label="Business people in an insurance meeting"></div><h3>insurance</h3></div>
  <div class="ind" style="left:0;top:1479px"><div class="photo" role="img" aria-label="Shopper in a supermarket aisle" style="background:linear-gradient(135deg,#8a6a4e,#3e3a36)"></div><h3>retail</h3></div>
  <div class="ind" style="left:400px;top:1479px"><div class="photo" role="img" aria-label="Truck on a highway" style="background:linear-gradient(180deg,#9aa9b8,#4b5663)"></div><h3>transportation</h3></div>
  <div class="ind" style="left:800px;top:1479px"><div class="photo" role="img" aria-label="Team collaborating in an office"></div><h3>workforce planning</h3></div>
</section>

<section>
  <h2 class="sec-title" style="top:1832px">what we do</h2>
  <p class="sec-lead" style="top:1896px">Mei an iracundia conceptam, cu agam cetero has, saperet partiendo posidonium mea ne. Sed idque persequeris accommodare cu. Eu imperdiet assueverit appellantur sea.</p>
  <div class="card" style="left:130px;top:2000px;height:262px">
    <svg viewBox="0 0 50 50" fill="none" stroke="#e84e1c" stroke-width="1.6"><rect x="8" y="5" width="26" height="36" rx="2"/><path d="M14 15h14M14 22h10M14 29h8M30 38l12-16 3 3-12 16-4 1z"/></svg>
    <h4 class="wrap">supply chain planning &amp; optimization</h4><div class="arrow">&rarr;</div>
  </div>
  <div class="card on" style="left:450px;top:2000px;height:262px">
    <svg viewBox="0 0 50 50" fill="none" stroke="#fff" stroke-width="1.6"><circle cx="13" cy="9" r="4"/><circle cx="25" cy="9" r="4"/><circle cx="37" cy="9" r="4"/><circle cx="25" cy="33" r="10"/><path d="M25 27v12M21 30h6M21 36h6"/></svg>
    <h4>workforce optimization</h4>
    <div class="link" style="margin-top:47px">Learn More <span class="pill"></span></div>
  </div>
  <div class="card" style="left:768px;top:2000px;height:262px">
    <svg viewBox="0 0 50 50" fill="none" stroke="#c22ad6" stroke-width="1.6"><path d="M25 8a12 12 0 0 0-7 22v6h14v-6a12 12 0 0 0-7-22zM19 41h12M25 18v10M8 12l4 3M42 12l-4 3"/></svg>
    <h4 class="wrap">rule based descision management</h4><div class="arrow">&rarr;</div>
  </div>
</section>

<section>
  <div class="how" role="img" aria-label="Person working at a computer in a dim office"></div>
  <div class="how-photo" role="img" aria-label="Woman looking at a screen in low light"></div>
  <div class="how-tab">HOW WE WORK</div>
  <div class="how-line"></div>
  <div class="step" style="left:134px"><span class="num">1</span>
    <svg width="40" height="40" viewBox="0 0 40 40" fill="none" stroke="#e84e1c" stroke-width="1.6"><path d="M6 32l20-24 6 5-20 24H6z"/></svg>
    <h5>initial analysis</h5><p>free of charge</p><div class="d">0.5-1 day</div></div>
  <div class="step" style="left:386px"><span class="num">2</span>
    <svg width="40" height="40" viewBox="0 0 40 40" fill="none" stroke="#c22ad6" stroke-width="1.6"><circle cx="20" cy="20" r="12"/><circle cx="20" cy="20" r="5"/></svg>
    <h5>scan</h5><p>we only charge 50%</p><div class="d">2-5 days</div></div>
  <div class="step" style="left:646px"><span class="num">3</span>
    <svg width="40" height="40" viewBox="0 0 40 40" fill="none" stroke="#c22ad6" stroke-width="1.6"><path d="M20 5l4 10 11 1-8 7 3 11-10-6-10 6 3-11-8-7 11-1z"/></svg>
    <h5>prototype</h5><p>we only charge 75%</p><div class="d">5-15 days</div></div>
  <div class="step" style="left:890px"><span class="num">4</span>
    <svg width="40" height="40" viewBox="0 0 40 40" fill="none" stroke="#c22ad6" stroke-width="1.6"><rect x="5" y="10" width="30" height="22" rx="2"/><path d="M5 16h30M12 22h6v6h-6z"/></svg>
    <h5>project</h5><p>execution of the project</p></div>
</section>

<section>
  <div class="tech-bg"></div>
  <h2 class="sec-title" style="top:2856px">technologies</h2>
  <p class="sec-lead" style="top:2920px">Mei an iracundia conceptam, cu agam cetero has, saperet partiendo posidonium mea ne. Sed idque persequeris accommodare cu. Eu imperdiet assueverit appellantur sea.</p>
  <div class="card tcard" style="left:130px;top:3007px">
    <svg viewBox="0 0 50 50" fill="none" stroke="#e84e1c" stroke-width="1.6"><path d="M6 44h34M10 44V30M17 44V24M24 44V28M31 44V18M8 22l10-8 8 5 14-10"/><circle cx="40" cy="38" r="6" stroke="#c22ad6"/></svg>
    <h4>advance analytics</h4><div class="arrow">&rarr;</div></div>
  <div class="card tcard on" style="left:450px;top:3007px">
    <svg viewBox="0 0 50 50" fill="none" stroke="#fff" stroke-width="1.6"><path d="M22 6a14 14 0 0 0-12 20l-2 8h6v8h12v-6"/><rect x="26" y="12" width="14" height="14"/><path d="M30 8v4M36 8v4M30 26v4M36 26v4M22 16h4M22 22h4M40 16h4M40 22h4"/></svg>
    <h4>artificial intelligence</h4>
    <div class="link" style="margin-top:14px">Learn More <span class="pill"></span></div></div>
  <div class="card tcard" style="left:768px;top:3007px">
    <svg viewBox="0 0 50 50" fill="none" stroke="#c22ad6" stroke-width="1.6"><rect x="19" y="4" width="12" height="10"/><rect x="5" y="34" width="10" height="10"/><rect x="20" y="34" width="10" height="10"/><rect x="35" y="34" width="10" height="10"/><path d="M25 14v10M10 34v-8h30v8M25 24v10"/></svg>
    <h4>rule based system</h4><div class="arrow">&rarr;</div></div>
  <div class="card tcard" style="left:130px;top:3235px">
    <svg viewBox="0 0 50 50" fill="none" stroke="#c22ad6" stroke-width="1.4"><circle cx="25" cy="25" r="4"/><circle cx="25" cy="8" r="3"/><circle cx="25" cy="42" r="3"/><circle cx="9" cy="16" r="3"/><circle cx="41" cy="16" r="3"/><circle cx="9" cy="34" r="3"/><circle cx="41" cy="34" r="3"/><path d="M25 11v10M25 29v10M12 17l10 6M38 17l-10 6M12 33l10-6M38 33l-10-6M9 19v12M41 19v12"/></svg>
    <h4>machine learning</h4><div class="arrow">&rarr;</div></div>
  <div class="card tcard" style="left:450px;top:3235px">
    <svg viewBox="0 0 50 50" fill="none" stroke="#c22ad6" stroke-width="1.6"><rect x="5" y="8" width="40" height="28" rx="2"/><path d="M18 44h14M25 36v8M11 28l8-8 6 5 12-12" stroke="#e84e1c"/></svg>
    <h4 style="letter-spacing:-.2px">mathmatical optimization</h4><div class="arrow">&rarr;</div></div>
  <div class="card tcard" style="left:768px;top:3235px">
    <svg viewBox="0 0 50 50" fill="none" stroke="#c22ad6" stroke-width="1.6"><path d="M8 18V8h12M42 32v10H30M8 8l8 8M42 42l-8-8"/><path d="M30 8h12v10M20 42H8V32" stroke="#e84e1c"/></svg>
    <h4>flexible architecture</h4><div class="arrow">&rarr;</div></div>
</section>

<section>
  <div class="testi">
    <h2>what our happy<br><b>CLIENT’S SAY</b></h2>
    <div class="link abs" style="left:110px;top:215px;font-size:12px">Read all Testimonials <span class="pill"></span></div>
  </div>
  <div class="quote-card">
    <span class="qm">”</span>
    <div class="who-line"><span class="avatar" role="img" aria-label="Client portrait"></span>
      <div><h6>MARTA RUIZ</h6><small>MANAGING DIRECTOR</small></div></div>
    <p>Lorem ipsum dolor sit amet, eius impetus et mel. Ubique facilisis has at. Usu ceteros voluptatum at, sea dicit euripidis reprimique ea. Id sea quaeque appareat voluptatibus, wisi splendide per cu.</p>
    <div class="pager"><i></i><i></i><i></i></div>
  </div>
</section>

<section>
  <div class="partners-label">Our Partners</div>
  <div class="plogo" style="left:130px"><i style="border-radius:50%"></i>Northwind</div>
  <div class="plogo" style="left:371px"><i></i>Lumentra</div>
  <div class="plogo" style="left:609px"><i></i>Postwave</div>
  <div class="plogo" style="left:848px"><i style="border-radius:50%"></i>Ringpath</div>
</section>

<section>
  <h2 class="sec-title" style="top:4280px">latest news &amp; blog</h2>
  <p class="sec-lead" style="top:4344px">Mei an iracundia conceptam, cu agam cetero has, saperet partiendo posidonium mea ne. Sed idque persequeris accommodare cu. Eu imperdiet assueverit appellantur sea.</p>
  <article class="news" style="left:130px" role="img" aria-label="Office scene">
    <div class="inner"></div>
    <div class="txt" style="bottom:85px"><small>01 DEC 2019</small><p>Strategic business and tax planning for all types of business entities</p>
      <div class="link">Read More <span class="pill"></span></div></div>
  </article>
  <article class="news" style="left:450px" role="img" aria-label="Woman with glasses reading a document">
    <div class="txt" style="bottom:55px"><small>01 DEC 2019</small><p>Strategic business and tax planning for all types of business entities</p></div>
  </article>
  <article class="news" style="left:769px;background:linear-gradient(160deg,#3c4a6a,#1f2433)" role="img" aria-label="Modern office with hanging lamps">
    <div class="txt" style="bottom:55px"><small>01 DEC 2019</small><p>Strategic business and tax planning for all types of business entities</p></div>
  </article>
</section>

<footer class="footer">
  <div class="brand abs" style="left:130px;top:105px">clarion <i></i></div>
  <div class="contact">
    <div><svg viewBox="0 0 14 14"><path d="M7 1a4 4 0 0 1 4 4c0 3-4 8-4 8S3 8 3 5a4 4 0 0 1 4-4z" fill="#e84e1c"/></svg><span>1420 Harbor Lane, Eastvale,<br>CA 92880</span></div>
    <div><svg viewBox="0 0 14 14"><path d="M3 1l3 3-2 2a8 8 0 0 0 4 4l2-2 3 3-2 2C6 13 1 8 1 3z" fill="#e84e1c"/></svg><span>Phone: 555-014-2290</span></div>
    <div><svg viewBox="0 0 14 14"><rect x="2" y="4" width="10" height="8" fill="#e84e1c"/><rect x="4" y="1" width="6" height="3" fill="#e84e1c"/></svg><span>Fax: 555-014-7731</span></div>
    <div><svg viewBox="0 0 14 14"><rect x="1" y="3" width="12" height="8" fill="#e84e1c"/></svg><span>E-Mail: <a>hello@clarion-ai.test</a></span></div>
  </div>
  <div class="form">
    <h6>LEAVE A MESSAGE</h6>
    <div class="row" style="margin-top:34px"><div class="field">First Name</div><div class="field">Last Name</div></div>
    <div class="row"><div class="field">Email Address</div></div>
    <div class="row"><div class="field" style="height:70px">Message</div></div>
    <div class="send">SEND MESSAGE <span class="pill"></span></div>
  </div>
  <div class="bottom">
    <span>Copyright © 2019. All Rights Reserved.&nbsp; Privacy Policy</span>
    <nav><span class="cur">Home</span><span>|</span><span>Resource</span><span>|</span><span>Partners</span><span>|</span><span>Contact Us</span></nav>
  </div>
</footer>

</body>
</html>
```